We need a Word Template for Custom Laboratory Results from an independent laboratory

The test is a novel biomarker for a chronic pain condition called endometriosis. It is expressed as a percentage. We will upload a sample result. We are looking for improved graphic fidelity with more attention to design and spacing. Emphasis should be placed on the overall result, i.e. the patient percentage results. Considerationis going to be given to the most appealing graphic result.

Target Market(s)

Women aged 19-45

Colors
0054AA
0677BA
7BADD7
CADEEF
E8F1F8

```html
<!DOCTYPE html>
<html lang="en">
<head>
<meta charset="utf-8">
<title>EndoSign Micro-RNA Endometriosis Assay – Results</title>
<link rel="stylesheet" href="https://fonts.googleapis.com/css2?family=Tinos:wght@400;700&family=Inter:wght@300;400;600&family=Montserrat:wght@500&display=swap">
<style>
  :root {
    --brand-blue: #3a60a8;
    --navy: #2b2d7e;
    --result-red: #c0172d;
    --clinic-grey: #555555;
    --clinic-teal: #5a9fae;
    --ink: #1a1a1a;
    --paper: #ffffff;
  }
  * { margin: 0; padding: 0; box-sizing: border-box; }
  html, body { width: 849px; height: 1200px; overflow: hidden; background: var(--paper); }
  .page { position: relative; width: 849px; height: 1200px; font-family: "Inter", sans-serif; color: var(--ink); }

  .clinic-mark { position: absolute; left: 42px; top: 48px; display: flex; align-items: center; gap: 14px; }
  .clinic-mark__dot { width: 72px; height: 72px; border-radius: 50%; background: var(--clinic-teal); }
  .clinic-mark__name { font-family: "Inter", sans-serif; font-weight: 400; font-size: 30px; color: var(--clinic-grey); }

  .lab-mark { position: absolute; right: 64px; top: 40px; font-family: "Inter", sans-serif; font-weight: 600; font-size: 52px; color: var(--brand-blue); letter-spacing: 1px; }

  .rule { position: absolute; left: 39px; width: 756px; height: 3px; background: var(--brand-blue); }

  .assay-title { position: absolute; left: 52px; top: 172px; font-family: "Tinos", serif; font-weight: 400; font-size: 37px; line-height: 46px; color: var(--brand-blue); letter-spacing: 0.5px; }

  .results-band { position: absolute; left: 39px; top: 285px; width: 756px; height: 38px; background: var(--brand-blue); }
  .results-band h2 { font-family: "Tinos", serif; font-weight: 700; font-size: 30px; line-height: 38px; color: #fff; padding-left: 14px; letter-spacing: 0.5px; }

  .field { position: absolute; display: flex; align-items: flex-end; }
  .field__label { font-size: 16px; font-weight: 300; text-align: right; margin-right: 14px; line-height: 21px; }
  .field__boxes { display: flex; height: 21px; border-bottom: 1px solid var(--brand-blue); border-left: 1px solid var(--brand-blue); }
  .field__boxes span { width: 20.5px; border-right: 1px solid var(--brand-blue); }

  .probability-caption { position: absolute; left: 43px; top: 508px; font-size: 15.5px; font-weight: 300; line-height: 21px; }

  .result-box { position: absolute; left: 411px; top: 497px; width: 384px; height: 146px; border: 2px solid var(--brand-blue); display: flex; justify-content: center; padding-top: 40px; }
  .result-box__value { font-family: "Inter", sans-serif; font-weight: 600; font-size: 40px; color: var(--result-red); line-height: 1; }

  .range-chart { position: absolute; left: 0; top: 690px; }
  .range-chart .tick-label { font-family: "Inter", sans-serif; font-size: 18px; fill: var(--navy); }
  .range-chart .band-label { font-family: "Montserrat", sans-serif; font-weight: 500; font-size: 14px; fill: var(--ink); }

  .reference { position: absolute; left: 89px; top: 993px; }
  .reference h3 { font-size: 16px; font-weight: 600; color: var(--brand-blue); line-height: 20px; }
  .reference ol { list-style: none; font-size: 13px; font-weight: 300; line-height: 17px; }
  .reference li span { display: inline-block; width: 25px; }
</style>
</head>
<body>
<div class="page">
  <div class="clinic-mark">
    <div class="clinic-mark__dot"></div>
    <div class="clinic-mark__name">Meridian Fertility</div>
  </div>
  <div class="lab-mark">Lumera Labs</div>

  <div class="rule" style="top:159px"></div>
  <h1 class="assay-title">ENDOSIGN MICRO-RNA<br>ENDOMETRIOSIS ASSAY</h1>
  <div class="rule" style="top:275px"></div>

  <div class="results-band"><h2>YOUR RESULTS</h2></div>

  <div class="field" style="left:30px; top:348px">
    <div class="field__label" style="width:107px">LAST NAME</div>
    <div class="field__boxes"><span></span><span></span><span></span><span></span><span></span><span></span><span></span><span></span><span></span><span></span><span></span><span></span><span></span><span></span><span></span><span></span><span></span><span></span><span></span><span></span><span></span><span></span></div>
  </div>
  <div class="field" style="left:30px; top:385px">
    <div class="field__label" style="width:107px">FIRST NAME</div>
    <div class="field__boxes"><span></span><span></span><span></span><span></span><span></span><span></span><span></span><span></span><span></span><span></span><span></span><span></span><span></span><span></span><span></span><span></span><span></span><span></span><span></span><span></span><span></span><span></span></div>
  </div>
  <div class="field" style="left:30px; top:422px">
    <div class="field__label" style="width:107px">OHIP NUMBER</div>
    <div class="field__boxes"><span></span><span></span><span></span><span></span><span></span><span></span><span></span><span></span><span></span><span></span><span></span><span></span></div>
  </div>
  <div class="field" style="left:400px; top:422px">
    <div class="field__label" style="width:45px">DOB</div>
    <div class="field__boxes"><span></span><span></span><span></span><span></span><span></span><span></span><span></span><span></span><span></span><span></span><span></span><span></span></div>
  </div>

  <div class="rule" style="top:480px"></div>

  <p class="probability-caption">Predicted Probability of Endometriosis Compared<br>to Surgical Controls (100% probability)</p>

  <div class="result-box"><span class="result-box__value">38.7%</span></div>

  <svg class="range-chart" width="849" height="270" viewBox="0 0 849 270" role="img" aria-label="Reference range bar chart">
    <g stroke="#000" stroke-width="1.2">
      <line x1="78" y1="28" x2="78" y2="252"/>
      <line x1="78" y1="252" x2="789" y2="252"/>
      <line x1="78" y1="28" x2="83" y2="28"/>
      <line x1="78" y1="73" x2="83" y2="73"/>
      <line x1="78" y1="118" x2="83" y2="118"/>
      <line x1="78" y1="163" x2="83" y2="163"/>
      <line x1="78" y1="207" x2="83" y2="207"/>
      <line x1="221" y1="252" x2="221" y2="246"/>
      <line x1="363" y1="252" x2="363" y2="246"/>
      <line x1="505" y1="252" x2="505" y2="246"/>
      <line x1="647" y1="252" x2="647" y2="246"/>
      <line x1="789" y1="252" x2="789" y2="246"/>
    </g>
    <g class="tick-label" text-anchor="end">
      <text x="74" y="35">100</text>
      <text x="72" y="80">80</text>
      <text x="72" y="125">60</text>
      <text x="72" y="170">40</text>
      <text x="72" y="214">20</text>
      <text x="78" y="260">0</text>
    </g>
    <g fill="var(--navy)">
      <rect x="99" y="185" width="102" height="67"/>
      <rect x="241" y="151" width="102" height="34"/>
      <rect x="383" y="128" width="102" height="23"/>
      <rect x="525" y="106" width="102" height="22"/>
      <rect x="667" y="28" width="102" height="78"/>
    </g>
    <g class="band-label" text-anchor="middle">
      <text x="152" y="186" dy="-13">0.0-29.9%</text>
      <text x="293" y="152" dy="-13">29.9-44.9%</text>
      <text x="435" y="129" dy="-13">45.0-55.0%</text>
      <text x="577" y="107" dy="-13">55.1-64.9%</text>
      <text x="721" y="29" dy="-10">65.0-99.9%</text>
    </g>
  </svg>

  <div class="rule" style="top:987px"></div>

  <section class="reference">
    <h3>Reference Range</h3>
    <ol>
      <li><span>1.</span>0.0-29.9% - &nbsp;low probability of endometriosis</li>
      <li><span>2.</span>29.9-44.9% - inconclusive</li>
      <li><span>3.</span>45.0-55.0% - intermediate risk of endometriosis</li>
      <li><span>4.</span>55.1-64.9% - probable endometriosis</li>
      <li><span>5.</span>65.0-99.9% - highly probable endometriosis</li>
    </ol>
  </section>

  <div class="rule" style="top:1137px"></div>
</div>
</body>
</html>
```